Varnel Solutions requires a new business card.

We are an online professional tool store.

Target Market(s)

We target the professional technician.

Industry/Entity Type

Business

Contact Information for Business Card

VarnelSolutions.com.au

sales@varnelsolutions.com

Requirements
Must have
• Needs to look commercial and professional
Should not have
• No Australian Colors, maps or shapes.
• No Shapes of Tools

```html
<!DOCTYPE html>
<html lang="en">
<head>
<meta charset="utf-8">
<title>Varnel Solutions – Business Card</title>
<link rel="stylesheet" href="https://fonts.googleapis.com/css2?family=Questrial&family=Montserrat:wght@600&display=swap">
<style>
  :root {
    --page: #e9ebef;
    --white: #ffffff;
    --blue: #2f4fc4;
    --blue-deep: #2540a8;
    --blue-light: #3d5fd6;
    --teal: #1aa6c4;
    --ink-blue: #2d46b8;
  }
  * { margin: 0; padding: 0; box-sizing: border-box; }
  html, body { width: 1200px; height: 780px; overflow: hidden; background: var(--page); }
  .stage { position: relative; width: 1200px; height: 780px; }

  .card {
    position: absolute; top: 100px; width: 340px; height: 580px;
    border-radius: 22px; overflow: hidden;
    box-shadow: 0 6px 18px rgba(20, 30, 70, 0.18);
    font-family: "Questrial", sans-serif;
  }
  .card-front { left: 190px; background: var(--white); }
  .card-back {
    left: 670px;
    background: radial-gradient(circle at 40% 45%, var(--blue-light) 0%, var(--blue) 55%, var(--blue-deep) 100%);
  }
  .card-art { position: absolute; inset: 0; width: 100%; height: 100%; }

  .brand { position: absolute; display: flex; align-items: center; gap: 10px; }
  .brand-dot { width: 34px; height: 34px; border-radius: 50%; flex: none; }
  .brand-name { font-family: "Questrial", sans-serif; font-size: 27px; letter-spacing: 0.5px; white-space: nowrap; }

  .card-front .brand { top: 98px; left: 0; right: 0; justify-content: center; }
  .card-front .brand-dot { background: var(--teal); }
  .card-front .brand-name { color: var(--ink-blue); }

  .contact { position: absolute; left: 0; right: 0; top: 278px; text-align: center; color: var(--white); }
  .person-name { font-family: "Montserrat", sans-serif; font-weight: 600; font-size: 24px; letter-spacing: 0.3px; }
  .person-role { font-size: 16px; }
  .rule { height: 1px; background: rgba(255,255,255,0.55); margin: 8px 34px; }
  .icon { display: block; margin: 0 auto 3px; width: 24px; height: 24px; }
  .contact-line { font-size: 16px; letter-spacing: 0.3px; }
  .address { font-size: 15px; line-height: 1.3; margin-top: 6px; }

  .website {
    position: absolute; left: 0; right: 0; bottom: 18px;
    text-align: center; color: var(--white); font-size: 17px; letter-spacing: 0.4px;
  }

  .back-title {
    position: absolute; left: 282px; top: 235px;
    transform: translate(-50%, -50%) rotate(-90deg);
    white-space: nowrap; color: var(--white);
    font-size: 36px; line-height: 1; letter-spacing: 2px; text-transform: uppercase;
  }
  .card-back .brand { left: 0; right: 0; bottom: 48px; justify-content: center; }
  .card-back .brand-dot { background: var(--white); width: 28px; height: 28px; }
  .card-back .brand-name { color: var(--white); font-size: 24px; }
</style>
</head>
<body>
<main class="stage">

  <section class="card card-front" aria-label="Business card front">
    <svg class="card-art" viewBox="0 0 340 580" aria-hidden="true">
      <path d="M0,225 Q170,215 340,300 L340,580 L0,580 Z" fill="#2f4fc4"/>
      <path d="M0,214 Q170,202 340,288 L340,300 Q170,215 0,225 Z" fill="#1aa6c4"/>
      <path d="M110,258 Q255,262 332,322" fill="none" stroke="#ffffff" stroke-opacity="0.7" stroke-width="1.5"/>
      <rect x="0" y="512" width="340" height="3" fill="#ffffff" fill-opacity="0.85"/>
      <rect x="0" y="515" width="340" height="65" fill="#1aa6c4"/>
    </svg>

    <div class="brand">
      <span class="brand-dot"></span>
      <span class="brand-name">Varnel Solutions</span>
    </div>

    <div class="contact">
      <p class="person-name">Daniel Hart</p>
      <p class="person-role">Founder</p>
      <div class="rule"></div>
      <svg class="icon" viewBox="0 0 24 24" aria-hidden="true">
        <circle cx="12" cy="12" r="11" fill="#ffffff"/>
        <path d="M7,9 Q12,5 17,9 L15.5,11 L13.5,10 L10.5,10 L8.5,11 Z M8.5,12 L15.5,12 L16.5,17 L7.5,17 Z" fill="#2f4fc4"/>
      </svg>
      <p class="contact-line">(123) 555-0148</p>
      <div class="rule"></div>
      <svg class="icon" viewBox="0 0 24 24" aria-hidden="true">
        <circle cx="12" cy="12" r="11" fill="#ffffff"/>
        <rect x="6.5" y="8" width="11" height="8" fill="none" stroke="#2f4fc4" stroke-width="1.4"/>
        <path d="M6.5,8 L12,12.5 L17.5,8" fill="none" stroke="#2f4fc4" stroke-width="1.4"/>
      </svg>
      <p class="contact-line">sales@varnelsolutions.com</p>
      <div class="rule"></div>
      <p class="address">PO BOX 482 Harbour Road<br>2nd street Kelvale</p>
    </div>

    <p class="website">VarnelSolutions.com.au</p>
  </section>

  <section class="card card-back" aria-label="Business card back">
    <p class="back-title">Varnel Solutions</p>
    <div class="brand">
      <span class="brand-dot"></span>
      <span class="brand-name">Varnel Solutions</span>
    </div>
  </section>

</main>
</body>
</html>
```